Anhänger für Pflanzset Basilikum und Schnittlauch
Bin mit der Arbeit von lumora sehr zufrieden. Der Designer war stets bemüht unsere Wünsche voll zu erfüllen. Die Lieferung der Rohdaten erfolgte zügig und problemlos. Gerne wieder!
Zielgruppe
Die Firma Kralvo bietet leckere biologische Köstlichkeiten mit nostalgischen Charme im BRUMM-Glas. Wir vertreiben u.a. Bio Kuchen, Bio Schoko-Fondues und Bio Backmischungen im Glas (www.kralvo-beispiel.de). Die Gläser werden mit 4c Etiketten auf dem Deckel und der Vorderseite individuell gestaltet. Auf der Rückseite stehen die Zutaten und gesetzlichen Pflichtangaben inklusive Bio/Grünhof Logo.
Das Design soll für Kunden sein, die ein nettes und nicht alltägliches Präsent suchen. Firmenkunden können optional ihr eigenes Logo mit auf dem Design platzieren. Endkunden können die Produkte in unserem Shop oder im Einzelhandel beziehen.
Wir produzieren unsere Produkte ausschließlich in Deutschland und verwenden regionale Rohstoffe wenn möglich. Kralvo ist Förderer von Stille Tafel Deutschland.
Aufgabenstellung
Für einen Anhänger in DIN A6 Hochformat für Pflanzsets suchen wir ein passendes Design.
Wir möchten den Konsumenten zu mehr nachhaltigen Konsum ermuntern und möchten, dass unsere Kuchen Gläser nach dem Gebrauch wiederverwendet werden. Dazu geben wir unseren Kunden z.B. auch Rezeptideen für das Einkochen oder Backen im Glas.
Zusätzlich möchten wir mit unseren Produkten im Glas kleine Pflanzsets anbieten. Der Gedanke dabei: Nach dem Verzehr des Inhalts soll die Pflanze in dem leeren Glas angepflanzt werden.
Im ersten Schritt bieten wir die Sorten Basilikum und Schnittlauch an. Das Pflanzsset befindet sich in einer Papiertüte aus Packpapier. Neben der Pflanzsensaat sind auch Erdquellscheiben und ein kleines Pflanzholz zur Beschriftung enthalten. Die Pflanzen werden in Bio Qualität angeboten.
Auf der Vorderseite des 110 x 153 mm Anhängers soll die entsprechende Pflanze (Basilikum oder Schnittlauch) abgebildet werden und der entsprechende Pflanzenname.
Auf der Rückseite Inhalt und Gebrauchsanweisung, z.B.
Saatset Basilikum
Inhalt: Basilikumsaat, 2 Erdscheiben & 1 Pflanzholz
Aussaat: Drinnen ganzjährig, im Freien von März - Juni
Wir hoffen, Sie haben mit unseren Produkten genau so viel Freude wie wir. Glas ist ein hochwertiger und nachhaltiger Rohstoff und kann problemlos wiederverwendet werden. Wie wäre beispielsweise Pflanzgefäß für diese Basilikum-Saat?
Einfach die Erdquellscheiben in etwas warmen Wasser aufweichen. Das so entstandene Substrat in das leere BRUMM-Glas füllen, Saat dünn auf die Erde auftreuen und mit etwas Erde abdecken. Achten Sie darauf, die Erde stets feucht zu halten. Nach ca. 2 Wochen beginnt die Pflanze zu wachsen.
Viel Erfolg bei der Aufzucht!
ACHTUNG: Die Kärtchen werden ca. 2, 5 cm vom oberen Rand gefalzt und an die Papiertüten gehängt. Daher sollte in diesem Bereich kein wichtiger Inhalt auftauchen.
Gern..

```html
<!DOCTYPE html>
<html lang="de">
<head>
<meta charset="utf-8">
<title>mein Kräuterwinkel – Anhänger</title>
<link href="https://fonts.googleapis.com/css2?family=Alegreya:wght@400;500&family=Almendra:wght@400;700&display=swap" rel="stylesheet">
<style>
  :root {
    --bg: #ffffff;
    --headline-green: #2e8a2c;
    --kraft: #cdb893;
    --kraft-dark: #b89f76;
    --ink-brown: #6a4a2b;
    --ink-soft: #8a6d4c;
    --leaf-green: #5e9a3a;
    --leaf-light: #a9cf7e;
    --jar: #e9e6dc;
    --badge-green: #5aa63a;
    --badge-grey: #7d7d7d;
  }
  * { margin: 0; padding: 0; box-sizing: border-box; }
  html, body { width: 1200px; height: 1200px; overflow: hidden; background: var(--bg); }
  .canvas { position: relative; width: 1200px; height: 1200px; }

  .headline {
    position: absolute; top: 150px; left: 0; width: 100%;
    text-align: center; color: var(--headline-green);
    font-family: "Alegreya", Georgia, serif; font-weight: 500;
    font-size: 46px; line-height: 1.3;
  }

  .tag-row {
    position: absolute; top: 360px; left: 60px; width: 1080px;
    display: flex; justify-content: space-between;
  }
  .tag {
    position: relative; width: 340px; height: 490px;
    background: linear-gradient(160deg, var(--kraft) 0%, var(--kraft-dark) 100%);
    color: var(--ink-brown); text-align: center;
    font-family: "Alegreya", Georgia, serif;
  }
  .tag__fold { height: 60px; border-bottom: 1px dashed rgba(106,74,43,.25); }
  .tag__series { font-size: 18px; margin-top: 8px; }
  .tag__name {
    font-family: "Almendra", Georgia, serif; font-weight: 700;
    font-size: 48px; line-height: 1.1; margin-top: 4px;
  }
  .tag__contents { font-size: 11px; color: var(--ink-soft); margin-top: 4px; }
  .tag__plant {
    width: 250px; height: 200px; margin: 12px auto 0;
    border-radius: 10px 10px 40px 40px;
    background: radial-gradient(ellipse at 50% 35%, var(--leaf-light) 0%, var(--leaf-green) 55%, var(--jar) 78%);
  }
  .tag__latin { font-family: "Almendra", Georgia, serif; font-size: 26px; margin-top: 12px; }
  .tag__claim { font-size: 14px; margin-top: 2px; }
  .tag__badges { position: absolute; right: 18px; bottom: 14px; display: flex; gap: 6px; }
  .badge { width: 26px; height: 18px; border-radius: 2px; }
  .badge--eu { background: var(--badge-green); }
  .badge--bio { background: var(--badge-grey); border-radius: 50%; width: 18px; }
</style>
</head>
<body>
<main class="canvas">
  <h1 class="headline">mein Kräuterwinkel<br>bio und frisch im BRUMM-Glas gezogen</h1>

  <section class="tag-row">
    <article class="tag">
      <div class="tag__fold"></div>
      <p class="tag__series">mein Kräuterwinkel</p>
      <h2 class="tag__name">schnittlauch</h2>
      <p class="tag__contents">Saatset · Erdquellscheiben · Pflanzholz</p>
      <div class="tag__plant" role="img" aria-label="Foto: Schnittlauch im Glas"></div>
      <p class="tag__latin">allium schoenoprasum</p>
      <p class="tag__claim">bio im BRUMM-Glas</p>
      <div class="tag__badges"><span class="badge badge--eu"></span><span class="badge badge--bio"></span></div>
    </article>

    <article class="tag">
      <div class="tag__fold"></div>
      <p class="tag__series">mein Kräuterwinkel</p>
      <h2 class="tag__name">thymian</h2>
      <p class="tag__contents">Saatset · Erdquellscheiben · Pflanzholz</p>
      <div class="tag__plant" role="img" aria-label="Foto: Thymian im Glas"></div>
      <p class="tag__latin">thymus vulgaris</p>
      <p class="tag__claim">bio im BRUMM-Glas</p>
      <div class="tag__badges"><span class="badge badge--eu"></span><span class="badge badge--bio"></span></div>
    </article>

    <article class="tag">
      <div class="tag__fold"></div>
      <p class="tag__series">mein Kräuterwinkel</p>
      <h2 class="tag__name">basilikum</h2>
      <p class="tag__contents">Saatset · Erdquellscheiben · Pflanzholz</p>
      <div class="tag__plant" role="img" aria-label="Foto: Basilikum im Glas"></div>
      <p class="tag__latin">ocimum basilicum</p>
      <p class="tag__claim">bio im BRUMM-Glas</p>
      <div class="tag__badges"><span class="badge badge--eu"></span><span class="badge badge--bio"></span></div>
    </article>
  </section>
</main>
</body>
</html>
```